50th Invite

Design a 50th birthday invite.

Key essentials to communicate are:

Date: 14 December 2019
Time: 7pm for 7.30pm departure
Birthday person: Glen
Theme: Boat Party
Location: Berth K4 27, Fernquay

Other than that will leave to your creativity. Just for clarity, the above is info to be communicated somehow on the invite, I dont want it to be simply copied.

i would like a luxury boat theme, think Miami, Bahamas etc etc, photos or drawings OK

```html
<!DOCTYPE html>
<html lang="en">
<head>
<meta charset="utf-8">
<title>Glen is turning 50 – Boat Party Invite</title>
<link rel="stylesheet" href="https://fonts.googleapis.com/css2?family=Sacramento&family=Dancing+Script:wght@500&family=Amaranth:wght@400;700&display=swap">
<style>
  :root {
    --sky-top: #b9d4de;
    --sky-mid: #a2c3d1;
    --horizon: #7098ad;
    --sea-deep: #1f4a68;
    --sea-dark: #123752;
    --hull-light: rgba(236, 242, 246, 0.85);
    --hull-shade: rgba(150, 172, 186, 0.55);
    --ink-blue: #1f5686;
    --white: #ffffff;
  }
  html, body {
    margin: 0;
    padding: 0;
    width: 1200px;
    height: 1200px;
    overflow: hidden;
  }
  .invite {
    position: relative;
    width: 1200px;
    height: 1200px;
    overflow: hidden;
  }
  .invite__photo {
    position: absolute;
    inset: 0;
    background: linear-gradient(180deg,
      var(--sky-top) 0%,
      var(--sky-mid) 42%,
      var(--horizon) 66%,
      var(--sea-deep) 70%,
      var(--sea-dark) 100%);
  }
  .invite__yacht {
    position: absolute;
    right: 0;
    bottom: 0;
    width: 400px;
    height: 640px;
    background: linear-gradient(200deg,
      rgba(255, 255, 255, 0) 0%,
      var(--hull-shade) 45%,
      var(--hull-light) 80%);
    clip-path: polygon(100% 0, 100% 100%, 0 100%, 20% 55%);
  }
  .invite__lead {
    position: absolute;
    top: 126px;
    left: 263px;
    width: 600px;
    text-align: center;
    margin: 0;
    font-family: "Dancing Script", cursive;
    font-weight: 500;
    font-size: 68px;
    line-height: 1.2;
    color: var(--ink-blue);
  }
  .invite__age {
    position: absolute;
    top: 255px;
    left: 248px;
    width: 600px;
    text-align: center;
    margin: 0;
    font-family: "Sacramento", cursive;
    font-weight: 400;
    font-size: 500px;
    line-height: 1;
    color: var(--white);
    transform: scaleX(0.81);
    transform-origin: center top;
  }
  .invite__tagline {
    position: absolute;
    top: 728px;
    left: 52px;
    margin: 0;
    font-family: "Amaranth", sans-serif;
    font-weight: 700;
    font-size: 31px;
    color: var(--ink-blue);
    transform: rotate(-8deg);
    transform-origin: left center;
    white-space: nowrap;
  }
  .details {
    position: absolute;
    top: 838px;
    left: 265px;
    width: 624px;
    height: 180px;
  }
  .details__grid {
    position: absolute;
    inset: 0;
  }
  .details__cell {
    position: absolute;
    height: 88px;
    display: flex;
    align-items: center;
    justify-content: center;
    font-family: "Amaranth", sans-serif;
    font-size: 26px;
    color: var(--white);
    margin: 0;
    white-space: nowrap;
  }
  .details__cell--day { left: 0; top: 0; width: 273px; }
  .details__cell--date { left: 273px; top: 0; width: 351px; }
  .details__cell--time { left: 0; top: 88px; width: 273px; font-size: 23px; }
  .details__cell--place { left: 273px; top: 88px; width: 351px; }
</style>
</head>
<body>
<main class="invite">
  <div class="invite__photo" role="img" aria-label="Photo of a man leaning out from the rail of a luxury sailing yacht over deep blue sea, pale sky and raindrops on the lens"></div>
  <div class="invite__yacht" role="img" aria-label="White hull, rails and teak deck of the luxury yacht on the right"></div>

  <h1 class="invite__lead">Glen is turning</h1>
  <p class="invite__age">50</p>
  <p class="invite__tagline">Lets celebrate him on a boat!!!</p>

  <section class="details" aria-label="Party details">
    <svg class="details__grid" width="624" height="180" viewBox="0 0 624 180" aria-hidden="true">
      <g stroke="#ffffff" stroke-width="3" fill="none">
        <line x1="0" y1="1.5" x2="624" y2="1.5"/>
        <line x1="0" y1="88" x2="624" y2="88"/>
        <line x1="0" y1="177" x2="624" y2="177"/>
        <line x1="273" y1="0" x2="273" y2="177"/>
      </g>
    </svg>
    <p class="details__cell details__cell--day">Saturday</p>
    <p class="details__cell details__cell--date">December 14, 2019</p>
    <p class="details__cell details__cell--time">7 for 7.30 PM Departure</p>
    <p class="details__cell details__cell--place">Berth K4 27, Fernquay</p>
  </section>
</main>
</body>
</html>
```